THE PRACTICE NAME "The Corvane MD" FOR A NEW MEDICAL PRACTICE STARTUP

THIS IS A BUSINESS CARD REQUEST FOR A KIDNEY DOCTOR's(NEPHROLOGIST) PRACTICE, THIS PRACTICE WILL BE IN EL PASO,TEXAS USA.OPEN TO INNOVATIVE IDEAS!

THE CORVANE MD ( NAME OF PRACTICE)

DEVESH R. MALHOTRA, MD FNKF FASN ( NAME OF PHYSICIAN WITH DEGREES)
BOARD CERTIFIED INTERNAL MEDICINE
BOARD CERTIFIED NEPHROLOGY
HYPERTENSION SPECIALIST

OFFICE ADDRESS, PHONE, FAX AND EMAIL PENDING

Healthy Kidneys. Better Lives.(MOTTO) THE LOGO SHOILD REFLECT THIS MESSAGE. WE NEED A LOGO DESIGN WITH 2 KIDNEYS OR CAN BE ONE KIDNEY ALSO.

Target Market(s)

PATIENTS WITH KIDNEY DISEASE, HYPERTENSION, ENGLISH AND SPANISH SPEAKING POPULATION AND PATIENTS ON DIALYSIS

Industry/Entity Type

Health Care

Contact Information for Business Card

HYPERTENSION SPECIALIST

WEBSITE URL PENDING

Font styles to use
Serif
Sans Serif
Script

Colors
fbed38
ffc214
fbf289
fbee3e
5c5c5c
333333
1b1b1b
757575
d3d3d3

Requirements
Must have
• A KIDNEY LOGO
• NAME OF THE PRACTICE
Nice to have
• IF THE CARD CAN BE IN THE SHAPE OF A KIDNEY

```html
<!DOCTYPE html>
<html lang="en">
<head>
<meta charset="utf-8">
<title>The Corvane MD – Business Card</title>
<link href="https://fonts.googleapis.com/css2?family=Lato:wght@300&family=Nunito:wght@800&family=Titillium+Web:wght@400;600&display=swap" rel="stylesheet">
<style>
  :root {
    --page-bg: #e4e4e4;
    --card-bg: #ffffff;
    --gold: #ffc214;
    --ink: #1b1b1b;
    --ink-soft: #333333;
    --mist: #ececec;
  }
  html, body {
    margin: 0;
    width: 1200px;
    height: 1200px;
    overflow: hidden;
    background: var(--page-bg);
  }
  .card {
    position: absolute;
    left: 112px;
    top: 304px;
    width: 990px;
    height: 576px;
    background: var(--card-bg);
    overflow: hidden;
  }
  .art-main {
    position: absolute;
    left: 8px;
    top: 0;
    width: 360px;
    height: 576px;
    background: var(--gold);
    border-radius: 0 0 110px 0;
  }
  .art-faint {
    position: absolute;
    left: 648px;
    top: 0;
    width: 342px;
    height: 356px;
    background: linear-gradient(160deg, var(--mist), #f6f6f6 80%);
    border-radius: 0 0 0 150px;
  }
  .brand-dot {
    position: absolute;
    left: 488px;
    top: 34px;
    width: 60px;
    height: 60px;
    border-radius: 50%;
    background: var(--gold);
  }
  .practice-name {
    position: absolute;
    left: 410px;
    top: 96px;
    margin: 0;
    font: 600 52px/1 "Titillium Web", sans-serif;
    color: var(--ink);
    white-space: nowrap;
  }
  .motto {
    position: absolute;
    left: 418px;
    top: 140px;
    margin: 0;
    font: 300 29px/1 "Lato", sans-serif;
    color: var(--gold);
    white-space: nowrap;
  }
  .physician {
    position: absolute;
    left: 408px;
    top: 206px;
    margin: 0;
    font: 800 34px/1 "Nunito", sans-serif;
    color: var(--ink);
    white-space: nowrap;
  }
  .physician .degrees {
    font-size: 20px;
    margin-left: 8px;
  }
  .credential {
    position: absolute;
    left: 410px;
    margin: 0;
    font: 400 25px/1 "Titillium Web", sans-serif;
    color: var(--ink-soft);
    white-space: nowrap;
  }
  .contact {
    position: absolute;
    margin: 0;
    font: 400 26px/1 "Titillium Web", sans-serif;
    color: var(--ink);
    white-space: nowrap;
    display: flex;
    align-items: center;
  }
  .contact svg {
    width: 28px;
    height: 28px;
    fill: var(--ink);
    margin-right: 14px;
  }
</style>
</head>
<body>
  <div class="card">
    <div class="art-main" role="img" aria-label="Large yellow kidney illustration"></div>
    <div class="art-faint" role="img" aria-label="Faint grey kidney illustration"></div>

    <div class="brand-dot"></div>
    <h1 class="practice-name">The Corvane MD</h1>
    <p class="motto">Healthy Kidneys. Better Lives.</p>

    <p class="physician">Devesh R. Malhotra,<span class="degrees">MD FNKF FASN</span></p>
    <p class="credential" style="top:246px">Board Certified Internal Medicine</p>
    <p class="credential" style="top:278px">Board Certified Nephrology</p>
    <p class="credential" style="top:310px">Hypertension Specialist</p>

    <p class="contact" style="left:410px; top:386px">
      <svg viewBox="0 0 24 24" aria-hidden="true"><path d="M6.6 10.8a15.1 15.1 0 0 0 6.6 6.6l2.2-2.2a1 1 0 0 1 1-.25 11.4 11.4 0 0 0 3.6.6 1 1 0 0 1 1 1V20a1 1 0 0 1-1 1A17 17 0 0 1 3 4a1 1 0 0 1 1-1h3.5a1 1 0 0 1 1 1c0 1.25.2 2.45.6 3.6a1 1 0 0 1-.25 1z"/></svg>
      1111-1111-1111
    </p>
    <p class="contact" style="left:676px; top:386px">
      <svg viewBox="0 0 24 24" aria-hidden="true"><path d="M6 2h12v5H6zM3 8h18a2 2 0 0 1 2 2v7h-4v5H5v-5H1v-7a2 2 0 0 1 2-2zm4 8v4h10v-4z"/></svg>
      1111-1111-1111
    </p>
    <p class="contact" style="left:410px; top:424px">
      <svg viewBox="0 0 24 24" aria-hidden="true"><path d="M2 5h20v14H2zm2 2v.4l8 5.3 8-5.3V7zm0 2.8V17h16V9.8l-8 5.3z"/></svg>
      your@emailaddress.com
    </p>
    <p class="contact" style="left:410px; top:462px">
      <svg viewBox="0 0 24 24" aria-hidden="true"><path d="M12 1a7 7 0 0 0-7 7c0 5.3 7 15 7 15s7-9.7 7-15a7 7 0 0 0-7-7zm0 9.5A2.5 2.5 0 1 1 12 5.5a2.5 2.5 0 0 1 0 5z"/></svg>
      Your Address, Line2&nbsp; Site# xxxx, City
    </p>
  </div>
</body>
</html>
```